Need a flyer to email blast investors, realtors and property owners offering my realty & property management services of the following....

I'm a Danfield Morrow agent offering an all service Real Estate & Property Management services to assist with buying, selling, renting & managing properties for owner of single family residence, multi family units, investment properties, HOA, seasonal equine rentals, vacation rentals and absentee owners.

Tenant Portal: Pay rent online, online application, tenant background criminal & eviction screening, search properties, sign lease online, view rent history and submit repairs and maintenance orders.

Owner Portal: Easy payment, financial statements, maintenance report and owners monthly and annual report.

Maintenance Portal: Conduct annual and move out inspections, create and generate work orders, easy communication with vendors and property managers, post photos directly into website for owner and tenant viewing.

Concierge service: for absentee owners we assist and offer groceries, personal shopping, car service & maintenance, property vendor access, maid service. seasonal rentals and airport pickup.

Offer an agent referral fee and 1st month property management fee FREE.

My company info..
Tolver Realty & Property Management
www,tolverrealtypm.example
555-318-4096

Target Market(s)

Realtors, investors, property owners, condos, investors and HOA

Industry/Entity Type

Property Management

Font styles to use
Decorative

Colors
86cfc6
33b8a4

Requirements
Must have
• I'm a Danfield Morrow agent offering an all service Real Estate & Property Management services to assist with buying, selling, renting & managing properties for owner of single family residence, multi family units, investment properties, HOA, seasonal equine rentals, vacation rentals and absentee owners.
• Tenant Portal: Pay rent online, online application, tenant background criminal & eviction screening, search properties, sign lease online, view rent history and submit repairs and maintenance orders.
• Owner Portal: Easy payment, financial statements, maintenance report and owners monthly and annual report.
• Maintenance Portal: Conduct annual and move out inspections, create and generate work orders, easy communication with vendors and property managers, post photos directly into website for owner and tenant viewing.
• Concierge service: for absentee owners we assist and offer groceries, personal shopping, car service & maintenance, property vendor access, maid service. seasonal rentals and airport pickup.
• Offer an agent referral fee and 1st month property management fee FREE.
• My company info..
• Tolver Realty & Property Management
• www,tolverrealtypm.example
• 555-318-4096
Nice to have
• pictures of happy people, houses, beaches, multi units.
Should not have
• n/a

```html
<!DOCTYPE html>
<html lang="en">
<head>
<meta charset="utf-8">
<title>Tolver Realty &amp; Property Management Flyer</title>
<link href="https://fonts.googleapis.com/css2?family=Oswald:wght@400;600;700&family=Open+Sans:ital,wght@0,600;0,700;0,800;1,700&display=swap" rel="stylesheet">
<style>
  :root {
    --teal: #33b8a4;
    --teal-light: #86cfc6;
    --teal-dark: #1f9a88;
    --ink: #2d2d2d;
    --paper: #ffffff;
  }
  * { margin: 0; padding: 0; box-sizing: border-box; }
  html, body { width: 900px; height: 1200px; overflow: hidden; background: var(--paper); }
  .flyer { position: relative; width: 900px; height: 1200px; background: var(--paper); font-family: "Open Sans", sans-serif; color: var(--ink); overflow: hidden; }
  .hero-photo { position: absolute; left: 0; top: 0; width: 900px; height: 330px; background: linear-gradient(120deg, #e9e2d6 0%, #d9c7ae 45%, #c9d6d2 100%); }
  .swoosh { position: absolute; left: 0; top: 0; width: 900px; height: 1200px; }
  .title-banner { position: absolute; left: 585px; top: 95px; width: 290px; height: 110px; background: var(--teal); border: 3px solid var(--paper); text-align: center; color: var(--paper); padding-top: 14px; }
  .title-banner .small { font-family: "Oswald", sans-serif; font-weight: 600; font-size: 19px; letter-spacing: 1.5px; text-transform: uppercase; }
  .title-banner .large { font-family: "Oswald", sans-serif; font-weight: 700; font-size: 44px; line-height: 52px; letter-spacing: 1px; }
  .headshot { position: absolute; left: 600px; top: 290px; width: 265px; height: 310px; border: 6px solid var(--paper); outline: 4px solid var(--teal); background: linear-gradient(160deg, #d8d0c4 0%, #8a6a52 55%, #3b2c24 100%); }
  .section-heading { font-family: "Oswald", sans-serif; font-weight: 600; font-size: 27px; color: var(--teal); text-transform: uppercase; letter-spacing: 1px; padding-bottom: 4px; border-bottom: 4px solid var(--teal); }
  .services { position: absolute; left: 32px; top: 380px; width: 535px; }
  .service { margin-top: 14px; }
  .service h3 { font-family: "Oswald", sans-serif; font-weight: 600; font-size: 23px; color: var(--teal); text-transform: uppercase; letter-spacing: .5px; line-height: 28px; }
  .service p { font-weight: 700; font-style: italic; font-size: 16px; line-height: 21px; }
  .about { position: absolute; left: 600px; top: 640px; width: 270px; }
  .about p { margin-top: 16px; font-weight: 700; font-style: italic; font-size: 17px; line-height: 24px; text-align: justify; }
  .skyline { position: absolute; left: 0; top: 1000px; width: 560px; height: 90px; background: linear-gradient(180deg, rgba(134,207,198,0) 0%, rgba(134,207,198,.3) 100%); }
  .contact { position: absolute; left: 32px; top: 1055px; color: var(--paper); }
  .contact h2 { font-family: "Oswald", sans-serif; font-weight: 600; font-size: 24px; text-transform: uppercase; letter-spacing: 1px; }
  .company { display: flex; align-items: center; gap: 10px; margin-top: 6px; font-weight: 700; font-size: 17px; line-height: 20px; width: 260px; }
  .company .mark { width: 30px; height: 30px; border-radius: 50%; background: var(--paper); flex: none; }
  .phone { position: absolute; left: 32px; top: 1128px; font-family: "Oswald", sans-serif; font-weight: 700; font-size: 54px; color: var(--paper); letter-spacing: 1px; }
  .website { position: absolute; right: 34px; top: 1160px; display: flex; align-items: center; gap: 8px; font-family: "Oswald", sans-serif; font-size: 21px; color: var(--teal); letter-spacing: 1.5px; }
  .website .dot { width: 16px; height: 16px; border-radius: 50%; background: var(--teal); }
</style>
</head>
<body>
<div class="flyer">
  <div class="hero-photo" role="img" aria-label="Photo of a smiling family of four relaxing together at home"></div>

  <svg class="swoosh" viewBox="0 0 900 1200" aria-hidden="true">
    <path d="M0 250 C 250 330, 520 240, 900 180 L900 300 C 600 310, 300 420, 0 360 Z" fill="var(--paper)"/>
    <path d="M0 270 C 260 350, 520 260, 900 200 L900 230 C 560 290, 280 380, 0 300 Z" fill="var(--teal)"/>
    <path d="M0 310 C 280 380, 560 300, 900 250 L900 268 C 560 320, 280 400, 0 330 Z" fill="var(--teal-light)"/>
    <path d="M0 1050 C 220 990, 500 1030, 900 1080 L900 1200 L0 1200 Z" fill="var(--teal-light)"/>
    <path d="M0 1040 C 240 1000, 520 1060, 900 1120 L900 1200 L0 1200 Z" fill="var(--teal)"/>
    <path d="M470 1200 C 600 1128, 760 1108, 900 1112 L900 1200 Z" fill="var(--paper)"/>
  </svg>

  <div class="title-banner">
    <div class="small">Tolver Realty &amp; Property</div>
    <div class="large">MANAGEMENT</div>
  </div>

  <div class="headshot" role="img" aria-label="Portrait photo of the agent"></div>

  <section class="services">
    <h2 class="section-heading">Our Services</h2>
    <div class="service">
      <h3>Tenant Portal:</h3>
      <p>Pay rent online, online application, tenant background criminal &amp; eviction screening, search properties, sign lease online, view rent history and submit repairs and maintenance orders.</p>
    </div>
    <div class="service">
      <h3>Owner Portal:</h3>
      <p>Easy payment, financial statements, maintenance report and owners monthly and annual report.</p>
    </div>
    <div class="service">
      <h3>Maintenance Portal:</h3>
      <p>Conduct annual and move out inspections, create and generate work orders, easy communication with vendors and property managers, post photos directly into website for owner and tenant viewing.</p>
    </div>
    <div class="service">
      <h3>Concierge Service:</h3>
      <p>for absentee owners we assist and offer groceries, personal shopping, car service &amp; maintenance, property vendor access, maid service, seasonal rentals and airport pickup.</p>
    </div>
    <div class="service">
      <h3>Special Offer:</h3>
      <p>Agent referral fee offered, and your 1st month property management fee is FREE.</p>
    </div>
  </section>

  <section class="about">
    <h2 class="section-heading">Who I Am</h2>
    <p>I'm a Danfield Morrow agent offering an all service Real Estate &amp; Property Management services to assist with buying, selling, renting &amp; managing properties for owner of single family residence, multi family units, investment properties, HOA, seasonal equine rentals, vacation rentals and absentee owners.</p>
  </section>

  <div class="skyline" role="img" aria-label="Faint illustration of houses and apartment buildings"></div>

  <div class="contact">
    <h2>Contact</h2>
    <div class="company"><span class="mark"></span><span>Tolver Realty &amp; Property Management</span></div>
  </div>
  <div class="phone">555-318-4096</div>

  <div class="website"><span class="dot"></span>www,tolverrealtypm.example</div>
</div>
</body>
</html>
```